Rising Stewards Scheme. Brochure to Inform Target Audience.

Rising Steward Scheme:

4 Page Brochure
Aimed at Parents and Children (Age 11-16)
Programme Overview
Specific Focus on Bronze Award with Learning Objectives and Enabling Objectives from Content Document
Contact Area Needed
How to Book - Online through the Website
Should encourage people to want to join it or sign up

you can use stock rugby images if needed

Target Market(s)

children between ages 11-16 and parents, gatekeepers (schools, rugby clubs)

Industry/Entity Type

Education

Font styles to use
Serif
Sans Serif

Requirements
Must have
• the programme content, each award continent and bronze award learning objectives
• Colours should match existing work that has been created
• Get in touch: www.valemark-rss.com
• maris@valemark-rss.com
Nice to have
• graphics of kids playing rugby if possible from stock images

```html
<!DOCTYPE html>
<html lang="en">
<head>
<meta charset="utf-8">
<title>Rising Stewards Scheme – Brochure Spread</title>
<link rel="stylesheet" href="https://fonts.googleapis.com/css2?family=Oswald:wght@500;600&family=Montserrat:wght@400;600;700&display=swap">
<style>
  :root{
    --ink:#1a1a1a;
    --black:#0b0b0b;
    --gold:#f5b800;
    --pitch:#3f7a2a;
    --pitch-dark:#22461a;
    --sky:#d9ecf7;
    --label:#3a3a3a;
    --paper:#ffffff;
  }
  *{box-sizing:border-box;margin:0;padding:0}
  html,body{width:1200px;height:903px;overflow:hidden;background:#fff}
  body{position:relative;font-family:"Montserrat",sans-serif;color:var(--ink)}
  .page-label{position:absolute;font:600 19px "Montserrat",sans-serif;color:var(--label);letter-spacing:.5px}
  .page{position:absolute;width:315px;height:408px;background:var(--paper);overflow:hidden;
        box-shadow:0 1px 4px rgba(0,0,0,.25)}
  .p1{left:238px;top:34px;background:var(--black)}
  .p2{left:648px;top:34px}
  .p5{left:238px;top:462px}
  .p4{left:648px;top:462px}

  /* cover */
  .cover-photo{position:absolute;left:0;top:110px;width:315px;height:298px;
    background:linear-gradient(180deg,#0b0b0b 0%,#1d2a12 38%,#4f7a20 62%,var(--pitch) 78%,#5d8f33 100%)}
  .cover-player{position:absolute;left:165px;top:110px;width:140px;height:245px;border-radius:60px 60px 20px 20px;
    background:linear-gradient(180deg,#1f5a35,#174a2c 60%,#e9e9e9 61%,#dcdcdc 75%,#1f5a35 76%)}
  .brand{position:absolute;left:40px;top:46px;width:95px;text-align:center}
  .brand-dot{width:30px;height:30px;border-radius:50%;background:var(--gold);margin:0 auto 4px}
  .brand-name{font:600 8px "Oswald",sans-serif;color:var(--gold);letter-spacing:.5px;line-height:1.1}
  .cover-title{position:absolute;left:19px;top:120px;font:500 19px "Oswald",sans-serif;color:var(--gold);line-height:1}
  .cover-sub{position:absolute;left:19px;top:142px;width:106px;display:flex;align-items:center;gap:4px;
    font:600 6px "Oswald",sans-serif;color:var(--gold);letter-spacing:2px}
  .cover-sub::before,.cover-sub::after{content:"";flex:1;height:1px;background:var(--gold)}
  .cover-head{position:absolute;left:19px;top:166px;font:500 22px "Oswald",sans-serif;line-height:1.27;color:#fff}
  .cover-head .hl{color:var(--gold)}
  .cover-url{position:absolute;left:16px;top:368px;font:400 9px "Montserrat",sans-serif;color:var(--gold)}
  .cover-band{position:absolute;left:0;bottom:0;width:315px;height:30px;background:#0b0b0b}
  .swoosh{position:absolute;left:0;width:315px;pointer-events:none}

  /* inner pages */
  .sect{position:absolute;left:15px;right:15px}
  .tab{display:flex;align-items:flex-end;height:9px;margin-bottom:4px;position:relative}
  .tab span{background:var(--black);color:#fff;font:600 6px "Montserrat",sans-serif;padding:1.5px 4px;line-height:1}
  .tab i{display:block;width:5px;height:9px;background:var(--gold);transform:skewX(-30deg);margin-left:-1px}
  .tab::after{content:"";flex:1;height:1px;background:var(--gold);margin-left:2px}
  .body{font:400 5.5px/1.36 "Montserrat",sans-serif;text-align:justify;color:#333}
  .body b{font-weight:700;color:#111}
  .photo{position:absolute;left:0;width:315px;background:linear-gradient(180deg,rgba(255,255,255,0) 0%,var(--sky) 18%,#b9d5c0 45%,var(--pitch) 75%,var(--pitch-dark) 100%)}
  .faq{position:absolute;top:136px;font:400 5.2px/1.36 "Montserrat",sans-serif;color:#333;text-align:justify}
  .faq b{display:block;font-weight:700;color:#111;margin-top:2px}
</style>
</head>
<body>

<div class="page-label" style="left:121px;top:390px">Page 1</div>
<div class="page-label" style="left:1010px;top:390px">Page 2</div>
<div class="page-label" style="left:121px;top:822px">Page 5</div>
<div class="page-label" style="left:1010px;top:822px">Page 4</div>

<!-- PAGE 1: cover -->
<section class="page p1">
  <div class="cover-photo" role="img" aria-label="Photo of a rugby player in green kit running with the ball on a stadium pitch"></div>
  <div class="cover-player" role="img" aria-label="Rugby player carrying the ball"></div>
  <svg class="swoosh" style="top:210px" width="315" height="110" viewBox="0 0 315 110">
    <path d="M0 100 C80 100 170 60 240 40 C275 30 300 28 315 28 L315 40 C290 40 260 48 230 60 C160 88 80 110 0 110Z" fill="var(--gold)"/>
  </svg>
  <div class="brand">
    <div class="brand-dot"></div>
    <div class="brand-name">VALEMARK<br>RUGBY</div>
  </div>
  <div class="cover-title">RISING STEWARDS</div>
  <div class="cover-sub">SCHEME</div>
  <div class="cover-head">LEARN TO LEAD<br><span class="hl">AND PLAY THE</span><br>VALEMARK WAY</div>
  <div class="cover-band"></div>
  <div class="cover-url">www.valemark-rss.com</div>
</section>

<!-- PAGE 2: overview -->
<section class="page p2">
  <div class="photo" style="top:205px;height:203px" role="img" aria-label="Photo of rugby players in red and green contesting a tackle at ground level"></div>
  <svg class="swoosh" style="top:340px" width="315" height="70" viewBox="0 0 315 70">
    <path d="M0 50 C80 30 160 30 230 48 C270 58 295 60 315 56 L315 66 C290 72 260 68 225 58 C150 40 80 42 0 62Z" fill="var(--gold)"/>
  </svg>
  <div class="sect" style="top:20px">
    <div class="tab"><span>Programme Overview</span><i></i></div>
    <p class="body">The Valemark have created a programme which enables each individual to maximise their learning potential so that you can be the best you can be. We provide a fun and healthy environment which is supported by highly motivated coaches which provide excellent individual care and attention. The programme is delivered over three Awards: Bronze, Silver and Gold.</p>
  </div>
  <div class="sect" style="top:76px">
    <div class="tab"><span>Bronze Award</span><i></i></div>
    <p class="body">The Bronze Award is focused on the 'Team' and is aimed at Children between the ages of 11 and 13. During the Award you will improve your self-confidence &amp; independence whilst having the opportunity to lead and inspire others. We will encourage your natural skills and help you identify any areas that you may wish to develop in the future. Each day we will build your skills through both physical and mental challenges both on and off the pitch. The Award is delivered over 5 days. Days 1 and 2 are delivered at the Home of Rugby, Harrowfield and days 3 to 5 are delivered at Ashbury Park.<br><b>Learning objectives:</b> teamwork, clear communication, self-confidence and leading others.</p>
  </div>
  <div class="sect" style="top:152px">
    <div class="tab"><span>Silver Award</span><i></i></div>
    <p class="body">On completion of the Bronze Award you are eligible to enrol on the Silver Award which is focused on the 'Individual'. This is aimed at 13 to 14 year olds and is again delivered over a 5 day period split between Harrowfield and Ashbury Park. During this award we will be empowering you to discover your own strengths and weakness in order to find your most natural leadership style so that we build transferrable skills for the future.</p>
  </div>
  <div class="sect" style="top:211px;left:122px">
    <div class="tab"><span>Gold Award</span><i></i></div>
    <p class="body">This is a 5 day residential course for all those who have successfully completed the Bronze and Silver Award. Aimed at 14+, this is the culmination of the Valemark Rising Stewards Scheme. During this award leaders will be challenged with a variety of practical exercises and on field activities in order to develop a rounded steward leader. Individuals will learn how to tackle complex problems and plan missions whilst feeling confident that they can lead others. These skills will equip them for their future learning and workplace environments.</p>
  </div>
</section>

<!-- PAGE 5: mission, values, FAQ -->
<section class="page p5">
  <div class="photo" style="top:240px;height:168px;left:110px;width:205px" role="img" aria-label="Photo of rugby players in green and gold jerseys competing for the ball"></div>
  <svg class="swoosh" style="top:330px" width="315" height="60" viewBox="0 0 315 60">
    <path d="M0 48 C90 40 170 20 240 14 C275 11 300 12 315 14 L315 24 C290 22 260 24 230 30 C160 44 80 56 0 58Z" fill="var(--gold)"/>
  </svg>
  <div class="sect" style="top:16px">
    <div class="tab"><span>Our Mission</span><i></i></div>
    <p class="body">To educate, inspire, mentor and transfer key leadership skills to the next generation</p>
  </div>
  <div class="sect" style="top:42px">
    <div class="tab"><span>Our Values</span><i></i></div>
    <p class="body"><b>Leadership.</b> For the team to be truly successful we believe in developing leadership at all levels.<br>
    <b>Courage.</b> We put the needs of the team ahead of their own.<br>
    <b>Selfless Commitment.</b> We have the physical and mental courage to possess confidence, bravery and resolution when faced with danger or fear.<br>
    <b>Resilience.</b> Our strength of character to overcome adversity and bounce back.<br>
    <b>Respect.</b> We respect those people who we train with and compete against. We believe in equal treatment and opportunity for all.</p>
  </div>
  <div class="sect" style="top:124px">
    <div class="tab"><span>Frequent Asked Questions</span><i></i></div>
  </div>
  <div class="faq" style="left:15px;width:140px">
    <b>Will you provide lunch or snacks?</b>Water will be provided to refill water bottles. However, we ask that children bring their own lunch.
    <b>Who attends your Rising Stewards Scheme?</b>Children of all abilities, some who have played rugby before and some who have never played. The programme is available to both boys and girls.
    <b>When do I drop and pick up my child from the programme?</b>Venue timings are included in your welcome letter. Typically the drop off time is 0900 and collection time at 1600. Please ensure your child is handed over and registered to one of our coaches on the programme before you leave.
    <b>What should my child wear?</b>Activities will take place both indoor and outdoor; therefore, please ensure you bring appropriate rugby kit, including waterproofs and a change of kit, also trainers and boots.
    <b>What makes your programme the right choice for my child?</b>The programme is fun and designed to develop the child's leadership skills on and off the pitch. These skills will help them grow as individuals.
  </div>
  <div class="faq" style="left:165px;width:135px">
    <b>How can I enrol on the silver or gold award?</b>In order to enrol on the Silver Award the child must have successfully completed the Bronze Award. In order to enrol on the Gold Award the child must have successfully completed the Silver Award.
    <b>Will I meet a Steward?</b>Yes. Whilst on the programme you will have a chance to meet and learn from a Steward.
    <b>How do you comply with safeguarding?</b>This is really important to us. We want all children to experience a fun, healthy and safe environment; therefore, our coaches and staff are educated and trained in safeguarding, child protection and are all DBS checked.
  </div>
</section>

<!-- PAGE 4: events and about -->
<section class="page p4">
  <div class="photo" style="top:226px;height:182px" role="img" aria-label="Photo of rugby players in green and gold jerseys running for the ball"></div>
  <svg class="swoosh" style="top:320px" width="315" height="70" viewBox="0 0 315 70">
    <path d="M0 56 C80 44 170 34 240 34 C275 34 300 36 315 40 L315 50 C290 46 260 44 230 46 C160 50 80 60 0 66Z" fill="var(--gold)"/>
  </svg>
  <div class="sect" style="top:19px">
    <div class="tab"><span>Events</span><i></i></div>
    <p class="body" style="text-align:left">The events will be scheduled through Eventora.com and therefore the API needs to be directed to the Website<br>
    <b>Bronze Award Part 1.</b> &nbsp;£179. &nbsp;22-23 October 2018. &nbsp;Harrowfield.<br>
    <b>Bronze Award Part 2.</b> &nbsp;£179. Ashbury Park. 21-23 February 2018<br>
    <b>Bronze Award Part 1 &amp; 2.</b> &nbsp;£299. 22-23 October and 21-23 February 2018</p>
  </div>
  <div class="sect" style="top:88px">
    <div class="tab"><span>Silver Award</span><i></i></div>
    <p class="body">Valemark Rugby, a world first is the fulfilment of a desire to create a colossal force for good. It emanates from the recognition and unification of rugby's finest warriors. This is a kinship of iconic men and women who have represented their countries in 100 international rugby test matches.</p>
    <p class="body" style="margin-top:6px">Only three in every 1000 international rugby players ever reach this massive milestone. As members of Valemark Rugby the Toughest Membership in the World; this rare and select breed of rugby players are uplifting lives by making the wonderful game more accessible and desirable to the growing number of rugby fans &amp; players across the globe. Valemark Rugby are luminaries, gladiators and warriors. But above all they are people. They have given so much. And now, as a unified force, they're giving back even more.</p>
    <p class="body" style="margin-top:6px">Valemark Rugby are luminaries, gladiators and warriors. But above all they are people. They have given so much. And now, as a unified force, they're giving back even more.<br><b>Learn More:</b> www.valemark-rss.com &nbsp; <b>Get in touch:</b> maris@valemark-rss.com</p>
  </div>
</section>

</body>
</html>
```